Business Card Design Project for Architecture and Interior Design company

We need a business card design and logo for an architecture and design firm located in Santiago de Chile. It´s a small company, and the name is "Ostrevo" ("Ostr" from my surname Ostrini, and "arq" for arquitectura or architecture. But it would also be nice that the logo comunicates de Word game "Bella" as beautiful in italian, and "arq" as architecture".
The idea is to give a delicate, elegant and sofisticated, yet fresh image. Would prefer grey black and white colors, but wouldn´t mind to use another additional color.
I allready have a web page www.ostrevo-studio.example, but would like to improve the logo design.
Please contact if any further information is requiered.
Reason: Need a more arquitectural and desing spirit in the cards. Few of them give that idea.

```html
<!DOCTYPE html>
<html lang="es">
<head>
<meta charset="utf-8">
<title>Ostrevo — Tarjeta de presentación</title>
<link rel="stylesheet" href="https://fonts.googleapis.com/css2?family=Jost:wght@200;400&display=swap">
<style>
  :root {
    --board: #bcbdbf;
    --charcoal: #4b4c4e;
    --paper: #ffffff;
    --logo-grey: #b4b5b7;
    --ink: #1d1d1f;
    --ink-soft: #5a5b5d;
    --shadow: rgba(40, 40, 42, 0.45);
  }
  * { margin: 0; padding: 0; box-sizing: border-box; }
  html, body {
    width: 934px;
    height: 1200px;
    overflow: hidden;
    background: var(--board);
    font-family: "Jost", "Futura", sans-serif;
  }
  .board { position: relative; width: 934px; height: 1200px; }

  .card {
    position: absolute;
    box-shadow: 6px 6px 6px var(--shadow);
  }

  .card--front {
    left: 211px;
    top: 250px;
    width: 514px;
    height: 285px;
    background: var(--charcoal);
    display: flex;
    align-items: center;
    justify-content: center;
  }
  .wordmark {
    font-weight: 200;
    font-size: 86px;
    letter-spacing: 0.2em;
    margin-right: -0.2em;
    color: var(--logo-grey);
    line-height: 1;
    margin-top: -8px;
  }

  .card--back {
    left: 209px;
    top: 626px;
    width: 516px;
    height: 287px;
    background: var(--paper);
    overflow: hidden;
  }
  .chevron {
    position: absolute;
    left: 0;
    top: 0;
    width: 516px;
    height: 287px;
  }
  .chevron path { fill: var(--charcoal); }

  .details {
    position: absolute;
    right: 26px;
    top: 134px;
    text-align: right;
  }
  .details__name {
    font-size: 16.5px;
    font-weight: 400;
    letter-spacing: 0.09em;
    color: var(--ink);
    text-transform: uppercase;
    line-height: 1;
  }
  .details__role {
    margin-top: 14px;
    font-size: 14px;
    letter-spacing: 0.2em;
    margin-right: -0.2em;
    color: var(--ink-soft);
    text-transform: uppercase;
    line-height: 1;
  }
  .details__contact {
    margin-top: 27px;
    font-size: 12.5px;
    line-height: 16px;
    color: var(--ink);
    font-style: normal;
  }
  .details__at {
    font-size: 8px;
    vertical-align: 4px;
  }
</style>
</head>
<body>
<main class="board">
  <section class="card card--front" aria-label="Anverso de la tarjeta">
    <h1 class="wordmark">ostrevo</h1>
  </section>

  <section class="card card--back" aria-label="Reverso de la tarjeta">
    <svg class="chevron" viewBox="0 0 516 287" aria-hidden="true">
      <path d="M0 0 H114 L188 142 L114 287 H0 Z"/>
    </svg>
    <div class="details">
      <p class="details__name">Lucia Ostrini Varela</p>
      <p class="details__role">Arquitecto</p>
      <address class="details__contact">
        +56 9 5550 1842<br>
        lostrini<span class="details__at">AT</span>ostrevo.example<br>
        www.ostrevo-studio.example
      </address>
    </div>
  </section>
</main>
</body>
</html>
```